Property Report - needs colour & design

We are a Commercial Real Estate Agency (Broker).
We have been commissioned to sell a property and require a presentation report to be sent to all potential purchasers.
The property is located in Sydney, Australia.
We have attached all the text (in word format) for the body of the report. The report should be in the same order as per the word document, this includes the position of photos, however, your input as to the layout and colour template for each page is what we are really looking for. I have uploaded a file of a previous report we prepared in-house to give you an idea of how we have presented our property reports in the past. I'd like to freshen-up this format with something more exciting but still easy to read.
What is needed is some design imagination which produces a clear an easy to follow report/presentation.
The main body of the report will only be around 6-8 pages.
Please find attached Images which should be in order as noted below and are to be placed on two separate pages at the end of the report:
Page 1
• External Image of the existing Building as is
• Perspective of DA approved conversion for Tully St
• Possible façade treatment for a commercial use

Page 2
• View from Level 1 over Harrowgate Park
• Internal image - level 1 of the existing building

```html
<!DOCTYPE html>
<html lang="en">
<head>
<meta charset="utf-8">
<title>Tully St &amp; Corliss St, Elmhurst – Auction</title>
<link href="https://fonts.googleapis.com/css2?family=Heebo:wght@300;400&display=swap" rel="stylesheet">
<style>
  :root {
    --ink-blue: #2c3b90;
    --band-blue: #2a3a8c;
    --auction-red: #d3202f;
    --paper: #ffffff;
    --sky-deep: #6a8fc4;
    --sky-light: #a7bcd8;
    --facade-light: #e4e2da;
    --facade-warm: #cfc3a4;
    --street-grey: #8c8c88;
  }
  * { margin: 0; padding: 0; box-sizing: border-box; }
  html, body { width: 848px; height: 1200px; overflow: hidden; background: var(--paper); }
  body { font-family: "Heebo", "Helvetica Neue", Arial, sans-serif; position: relative; }

  .property-title {
    position: absolute; left: 58px; top: 44px;
    color: var(--ink-blue); font-weight: 300;
    font-size: 48px; line-height: 54px; letter-spacing: -0.5px;
  }
  .site-status {
    position: absolute; left: 60px; top: 246px;
    color: var(--auction-red); font-weight: 300; font-size: 29px;
  }

  .auction-badge {
    position: absolute; left: 541px; top: 93px;
    width: 234px; height: 234px; border-radius: 50%;
    background: var(--auction-red); color: var(--paper);
    text-align: center; font-weight: 300;
  }
  .auction-badge .badge-heading { position: absolute; top: 16px; width: 100%; font-size: 43px; line-height: 50px; letter-spacing: 0.5px; }
  .auction-badge .badge-date { position: absolute; top: 70px; width: 100%; font-size: 18px; line-height: 22px; }
  .auction-badge .badge-rule { position: absolute; top: 109px; left: 20px; right: 20px; border-top: 1.5px solid var(--paper); }
  .auction-badge .badge-note { position: absolute; top: 120px; width: 100%; font-size: 25px; line-height: 30px; }

  .render-band {
    position: absolute; left: 0; top: 357px; width: 848px; height: 606px;
    border-top: 6px solid var(--band-blue); border-bottom: 6px solid var(--band-blue);
  }
  .render-band .render-area {
    width: 100%; height: 100%;
    background:
      radial-gradient(ellipse 70% 45% at 55% 55%, rgba(214,190,120,0.45) 0%, rgba(214,190,120,0) 70%),
      linear-gradient(180deg, var(--sky-deep) 0%, var(--sky-light) 26%, var(--facade-light) 48%, var(--facade-warm) 66%, var(--street-grey) 100%);
  }

  .agent {
    position: absolute; left: 60px; top: 1066px;
    color: var(--ink-blue); font-weight: 300; font-size: 36px; line-height: 42px;
  }
  .agent .agent-name { font-weight: 400; }

  .agency-name {
    position: absolute; left: 522px; top: 1062px;
    display: flex; align-items: center; gap: 14px;
    color: var(--band-blue); font-weight: 400; font-size: 30px; line-height: 32px;
  }
  .agency-name .agency-mark { width: 56px; height: 56px; background: var(--auction-red); flex: none; }
</style>
</head>
<body>
  <h1 class="property-title">44-56 Tully St &amp;<br>19 Corliss St,<br>ELMHURST</h1>
  <p class="site-status">DA Approved Site</p>

  <div class="auction-badge">
    <div class="badge-heading">AUCTION</div>
    <div class="badge-date">Tues, 3 Dec 2013</div>
    <div class="badge-rule"></div>
    <div class="badge-note">If not sold prior</div>
  </div>

  <div class="render-band">
    <div class="render-area" role="img" aria-label="Architectural perspective render of the DA approved six-storey mixed-use building with white and ochre façade, timber screens and glazed balconies, on the corner of Corliss Street and a future public laneway, annotated with façade finishes"></div>
  </div>

  <div class="agent">
    <div class="agent-name">Daniel Morrow</div>
    <div class="agent-phone">0412 555 018</div>
  </div>

  <div class="agency-name">
    <span class="agency-mark"></span>
    <span>HARBOURLINE<br>PROPERTY</span>
  </div>
</body>
</html>
```